Brilliant Design Needed For Stand Up Pouch - Drink Mix

We need a layout for our resealable stand-up pouch that holds our powered sports drink mix. Target audience is endurance athletes that enjoy marathon running, cycling, mountain biking, hiking and triathlon. Secondary audience are participants in team sports such soccer, lacrosse, football and basketball. Please review the attached project brief for full details. Thanks!

Target Market(s)

50/50 male/female, ages 20-50, USA, succesful, driven, educated. Active, healthy, athletic, outdoor lifestyle.

Industry/Entity Type

Fitness

Font styles to use
Sans Serif

Colors
33a6d7
3277b5
abd037

Requirements
Must have
• Please review the attached project brief for full details.
Nice to have
Should not have

```html
<!DOCTYPE html>
<html lang="en">
<head>
<meta charset="utf-8">
<title>PeakTide Hydration Drink Mix – Pouch Range</title>
<link href="https://fonts.googleapis.com/css2?family=Saira+Condensed:wght@500;600;700&family=Exo+2:ital,wght@0,400;0,600;0,700;1,600&family=Tinos:ital@1&display=swap" rel="stylesheet">
<style>
  :root {
    --bg: #9fcbe8;
    --navy: #1d3560;
    --brand-blue: #3277b5;
    --sky: #33a6d7;
    --green: #56ad2c;
    --green-light: #abd037;
    --grey: #c8ccd1;
    --grey-dark: #a9aeb5;
    --white: #ffffff;
    --ink: #3a4150;
    --muted: #5a606b;
  }
  * { box-sizing: border-box; margin: 0; padding: 0; }
  html, body { width: 1200px; height: 808px; overflow: hidden; }
  body { background: var(--bg); position: relative; font-family: "Exo 2", sans-serif; }

  .pouch {
    position: absolute; top: 163px; width: 326px; height: 566px;
    background: var(--white);
    border-radius: 16px 16px 8px 8px;
    overflow: hidden;
  }
  .pouch--sports { left: 81px; }
  .pouch--endurance { left: 437px; }
  .pouch--ultra { left: 787px; }

  .pouch__green-band {
    position: absolute; left: 14px; top: 306px; width: 300px; height: 112px;
    background: var(--green);
  }
  .pouch__photo {
    position: absolute; left: 134px; top: 6px; width: 184px; height: 302px;
  }
  .pouch--sports .pouch__photo { background: linear-gradient(180deg, #2a6cb8 0%, #4f92d2 50%, #3f6a3a 78%, #9a4a3c 100%); }
  .pouch--endurance .pouch__photo { background: linear-gradient(180deg, #9ab8d4 0%, #6f8ca3 40%, #45633a 72%, #2f4a22 100%); }
  .pouch--ultra .pouch__photo { background: linear-gradient(180deg, #1e4ea6 0%, #4f7cc0 40%, #6c6b66 70%, #403c37 100%); }

  .pouch__side {
    position: absolute; left: 34px; top: 0; width: 100px; height: 420px;
    background: linear-gradient(90deg, var(--grey-dark), var(--grey) 40%, #dfe2e5);
  }
  .pouch__mark {
    position: absolute; left: 12px; top: 24px;
    display: flex; align-items: center; gap: 5px;
    font-family: "Saira Condensed", sans-serif; font-weight: 700;
    font-size: 18px; line-height: 1; color: var(--brand-blue);
  }
  .pouch__mark-square { width: 11px; height: 11px; background: var(--brand-blue); }
  .pouch__brand {
    position: absolute; left: 10px; bottom: 38px;
    writing-mode: vertical-rl; transform: rotate(180deg);
    font-family: "Saira Condensed", sans-serif; font-weight: 700;
    font-size: 50px; line-height: 1; letter-spacing: 1px;
    color: var(--brand-blue);
  }
  .pouch__system {
    position: absolute; left: 60px; bottom: 90px;
    writing-mode: vertical-rl; transform: rotate(180deg);
    font-family: "Tinos", serif; font-style: italic;
    font-size: 18px; color: var(--navy); white-space: nowrap;
  }

  .pouch__label {
    position: absolute; left: 146px; top: 312px; width: 170px;
    color: var(--white);
  }
  .pouch__title {
    font-family: "Saira Condensed", sans-serif; font-weight: 700;
    font-size: 38px; line-height: 1; letter-spacing: .5px;
    text-shadow: 1px 1px 0 var(--navy); white-space: nowrap;
  }
  .pouch__subtitle {
    font-family: "Saira Condensed", sans-serif; font-weight: 600;
    font-size: 22px; line-height: 1; text-align: center; width: 160px;
    text-shadow: 1px 1px 0 var(--navy);
  }
  .pouch__flavor {
    font-family: "Exo 2", sans-serif; font-style: italic; font-weight: 600;
    font-size: 12.5px; line-height: 1.55; margin-top: 2px;
  }

  .pouch__info { position: absolute; left: 40px; top: 428px; width: 270px; color: var(--navy); }
  .pouch__range {
    font-family: "Saira Condensed", sans-serif; font-weight: 600;
    font-size: 21px; line-height: 1; letter-spacing: .3px; white-space: nowrap;
    padding-bottom: 4px; border-bottom: 2px solid var(--navy); display: inline-block;
  }
  .pouch__formula {
    font-family: "Saira Condensed", sans-serif; font-weight: 600;
    font-size: 22px; line-height: 1.1; letter-spacing: 1.5px; color: var(--ink);
    text-align: center; width: 240px; white-space: nowrap; margin-top: 5px;
  }
  .pouch__usage { font-size: 10.5px; color: var(--muted); line-height: 1.35; margin-top: 3px; white-space: nowrap; }
  .pouch__servings { font-weight: 700; font-size: 14px; margin: 6px 0 0 26px; white-space: nowrap; }
  .pouch__weight {
    font-family: "Saira Condensed", sans-serif; font-weight: 600;
    font-size: 11px; text-align: right; margin-top: 8px; padding-right: 8px;
  }
</style>
</head>
<body>

<section class="pouch pouch--sports">
  <div class="pouch__green-band"></div>
  <div class="pouch__photo" role="img" aria-label="Woman sprinting on a running track under blue sky"></div>
  <div class="pouch__side">
    <div class="pouch__mark"><span class="pouch__mark-square"></span>PEAKTIDE</div>
    <span class="pouch__brand">PEAKTIDE</span>
    <span class="pouch__system">Advanced Hydration System</span>
  </div>
  <div class="pouch__label">
    <div class="pouch__title">HYDRATION</div>
    <div class="pouch__subtitle">DRINK MIX</div>
    <div class="pouch__flavor">Lemon Lime with other<br>flavors</div>
  </div>
  <div class="pouch__info">
    <div class="pouch__range">ADVANCED HYDRATION SYSTEM</div>
    <div class="pouch__formula">SPORTS FORMULA</div>
    <div class="pouch__usage">Recommended for workouts lasting 1 hours<br>or more</div>
    <div class="pouch__servings">Makes 27, 12 fl oz Servings</div>
    <div class="pouch__weight">NET WT. 15.5 OZ (440G)</div>
  </div>
</section>

<section class="pouch pouch--endurance">
  <div class="pouch__green-band"></div>
  <div class="pouch__photo" role="img" aria-label="Mountain biker riding down a grassy alpine trail"></div>
  <div class="pouch__side">
    <div class="pouch__mark"><span class="pouch__mark-square"></span>PEAKTIDE</div>
    <span class="pouch__brand">PEAKTIDE</span>
    <span class="pouch__system">Advanced Hydration System</span>
  </div>
  <div class="pouch__label">
    <div class="pouch__title">HYDRATION</div>
    <div class="pouch__subtitle">DRINK MIX</div>
    <div class="pouch__flavor">Lemon Lime with other<br>flavors</div>
  </div>
  <div class="pouch__info">
    <div class="pouch__range">ADVANCED HYDRATION SYSTEM</div>
    <div class="pouch__formula">ENDURANCE FORMULA</div>
    <div class="pouch__usage">Recommended for workouts lasting 2 hours<br>or more</div>
    <div class="pouch__servings">Makes 27, 12 fl oz Servings</div>
    <div class="pouch__weight">NET WT. 15.5 OZ (440G)</div>
  </div>
</section>

<section class="pouch pouch--ultra">
  <div class="pouch__green-band"></div>
  <div class="pouch__photo" role="img" aria-label="Hiker with backpack resting on a rocky mountain summit"></div>
  <div class="pouch__side">
    <div class="pouch__mark"><span class="pouch__mark-square"></span>PEAKTIDE</div>
    <span class="pouch__brand">PEAKTIDE</span>
    <span class="pouch__system">Advanced Hydration System</span>
  </div>
  <div class="pouch__label">
    <div class="pouch__title">HYDRATION</div>
    <div class="pouch__subtitle">DRINK MIX</div>
    <div class="pouch__flavor">Lemon Lime with other<br>flavors</div>
  </div>
  <div class="pouch__info">
    <div class="pouch__range">ADVANCED HYDRATION SYSTEM</div>
    <div class="pouch__formula">ULTRA FORMULA</div>
    <div class="pouch__usage">Recommended for workouts lasting 3 hours<br>or more</div>
    <div class="pouch__servings">Makes 27, 12 fl oz Servings</div>
    <div class="pouch__weight">NET WT. 15.5 OZ (440G)</div>
  </div>
</section>

</body>
</html>
```